Book Cover Design Book About Commercial Real Estate Investing

I need a book cover designed for my upcoming book.
Need cover for paperback and hardcover book.

The Book is about investing in net lease commercial property.

The book title:

The Ground Rent Handbook
Proven Methods For KVR Asset Buyers
By Lou Barrow

Should be minimalist, clean, authoritative, convey money, trust, & growth
I think I like the colors white red and black.
I want a front cover at this time.

Samples I like are included. - the red white and blacks are my favorites

My company is The KVR Circle
you can learn more about Triple Net Properties at my website
www.TheKVRCircle.com

the symbol NNN = Triple net in commercial real estate

Target Market(s)

Affluent male conservative investors

Industry/Entity Type

Real Estate

Requirements
Nice to have
• Sports Motif - - diagrams of sports plays from playbook
• google - Diagrams of sports plays -

```html
<!DOCTYPE html>
<html lang="en">
<head>
<meta charset="utf-8">
<title>The Ground Rent Handbook – Book Cover</title>
<link rel="stylesheet" href="https://fonts.googleapis.com/css2?family=Oswald:wght@300;500;600&family=Open+Sans:wght@300;400&display=swap">
<style>
  :root {
    --red: #ec2227;
    --black: #050505;
    --white: #ffffff;
    --accent-green: #3fa845;
  }
  html, body {
    margin: 0;
    padding: 0;
    width: 1200px;
    height: 733px;
    overflow: hidden;
    background: var(--white);
  }
  .cover {
    display: block;
    width: 1200px;
    height: 733px;
  }
  .title-face { font-family: "Oswald", sans-serif; font-weight: 300; }
  .label-face { font-family: "Oswald", sans-serif; font-weight: 600; }
  .body-face { font-family: "Open Sans", sans-serif; }
  .fill-red { fill: var(--red); }
  .fill-black { fill: var(--black); }
  .fill-white { fill: var(--white); }
  .fill-accent { fill: var(--accent-green); }
</style>
</head>
<body>
<svg class="cover" viewBox="0 0 1200 733" xmlns="http://www.w3.org/2000/svg" role="img" aria-label="Book cover wrap for The Ground Rent Handbook by Lou Barrow">

  <!-- page bands -->
  <rect class="fill-white" x="0" y="0" width="1200" height="733"/>
  <rect class="fill-black frame-top" x="0" y="0" width="1200" height="30"/>
  <rect class="fill-black frame-bottom" x="0" y="697" width="1200" height="36"/>

  <!-- back cover -->
  <g class="back-cover">
    <rect class="fill-red" x="0" y="30" width="555" height="667"/>
    <text class="body-face fill-white back-tagline" x="268" y="60" font-size="16" font-weight="400" text-anchor="middle">Triple net in commercial real estate</text>
    <text class="title-face fill-black back-title-top" x="187" y="580" font-size="32" textLength="186" lengthAdjust="spacingAndGlyphs">THE GROUND RENT</text>
    <text class="title-face fill-white back-title-main" x="187" y="628" font-size="55" textLength="186" lengthAdjust="spacingAndGlyphs">HANDBOOK</text>
    <g class="publisher-tab">
      <polygon class="fill-black" points="198,697 358,697 358,657 278,640 198,657"/>
      <rect class="fill-accent" x="212" y="674" width="13" height="13"/>
      <text class="label-face fill-white" x="232" y="687" font-size="16" textLength="112" lengthAdjust="spacingAndGlyphs">THE KVR CIRCLE</text>
    </g>
  </g>

  <!-- spine -->
  <g class="spine">
    <rect class="fill-red" x="555" y="262" width="93" height="200"/>
    <g class="author-tab">
      <polygon class="fill-black" points="568,30 645,30 645,140 606,152 568,140"/>
      <text class="label-face fill-white" transform="translate(611 90) rotate(-90)" font-size="14" text-anchor="middle">BY LOU BARROW</text>
    </g>
    <g class="spine-title" transform="translate(0 460) rotate(-90)">
      <text class="title-face fill-black" x="3" y="590" font-size="35" textLength="194" lengthAdjust="spacingAndGlyphs">THE GROUND RENT</text>
      <text class="title-face fill-white" x="3" y="642" font-size="60" textLength="194" lengthAdjust="spacingAndGlyphs">HANDBOOK</text>
    </g>
    <g class="publisher-tab">
      <polygon class="fill-black" points="560,697 637,697 637,622 598,605 560,622"/>
      <text class="label-face fill-white" transform="translate(604 670) rotate(-90)" font-size="14" text-anchor="middle" textLength="96" lengthAdjust="spacingAndGlyphs">THE KVR CIRCLE</text>
    </g>
  </g>

  <!-- front cover -->
  <g class="front-cover">
    <rect class="fill-red title-band" x="648" y="262" width="552" height="200"/>
    <g class="publisher-tab">
      <polygon class="fill-black" points="875,30 1035,30 1035,108 955,125 875,108"/>
      <rect class="fill-accent" x="887" y="62" width="15" height="15"/>
      <text class="label-face fill-white" x="909" y="78" font-size="19" textLength="114" lengthAdjust="spacingAndGlyphs">THE KVR CIRCLE</text>
    </g>
    <text class="title-face fill-black front-title-top" x="655" y="345" font-size="84" textLength="535" lengthAdjust="spacingAndGlyphs">THE GROUND RENT</text>
    <text class="title-face fill-white front-title-main" x="655" y="462" font-size="137" textLength="535" lengthAdjust="spacingAndGlyphs">HANDBOOK</text>
    <text class="body-face fill-black front-subtitle" x="657" y="494" font-size="27" font-weight="300" textLength="530" lengthAdjust="spacingAndGlyphs">Proven Methods For KVR Asset Buyers</text>
    <g class="author-tab">
      <polygon class="fill-black" points="875,697 1035,697 1035,650 955,633 875,650"/>
      <text class="label-face fill-white" x="955" y="669" font-size="16" text-anchor="middle">BY</text>
      <text class="label-face fill-white" x="955" y="690" font-size="16" text-anchor="middle">LOU BARROW</text>
    </g>
  </g>
</svg>
</body>
</html>
```